Modern and strong website design for a Dutch crowdsourcing company
.

We are startup company providing crowdsourcing of administrative and customers service tasks for larger companies and other organizations. We offer cost savings and scale-ability combined with higher quality of execution. We will soon enter the market and need a website that has two major target groups: 1. Our corporate customers 2. The mainly younger crowd executing the tasks on our platform.
The target group of customers are Influencers and decision makers with companies and other organizations in with large administrative and customer service departments. Most information in the startup phase will be targeting this group.
The target group of future crowd workers will be heterogeneous, from students to stay at home mums or night shift workers who want to earn some extra money by performing easy to execute microtasks in the cloud. We will target both Dutch and international workers.

The website must be developed for browsing on a computer but also be optimized for mobile devices and tablets.
The website must be optimized and tested for the major browsers on windows, macOS and mobile devices.

For the minimum requirement for the website see attached wireframes

The present landing page http://bravolinkhive.com and logo are not reflecting our preferences!
See enclosed a new logo that stands for both the crowdwork (performed for our customers) and the crowd (a hive in motion).

Target Market(s)

see tekst above.

Industry/Entity Type

Business Service

Coding

Coded - Design and coding required

Number of Pages Required

5+ page

Font styles to use
Sans Serif
Other font styles liked:
• Lato, Open Sans

Colors

Designer to choose colors to be used in the design.

Requirements
Must have
• start devider screen
• home page displaying business and worker information
• a page displaying only info for businesses
• a page displaying only info for workers
• a contact form
• a reviews page
• color scheme from logo
• responsiveness!
Nice to have
• Nice animations
• overlapping blocks, animated on scroll
• lightbox effects if applicable
• animated mobile menu icon and menu itself

```html
<!DOCTYPE html>
<html lang="en">
<head>
<meta charset="utf-8">
<title>A Hive in Motion</title>
<link href="https://fonts.googleapis.com/css2?family=Questrial&family=Raleway:wght@400&display=swap" rel="stylesheet">
<style>
  :root {
    --ink: #ffffff;
    --accent: #f58a1f;
    --rule: rgba(255, 255, 255, 0.75);
    --veil: rgba(20, 20, 22, 0.78);
    --pill-fill: rgba(8, 8, 8, 0.55);
    --pill-edge: rgba(220, 220, 220, 0.7);
    --tile-a: #6d5a4d;
    --tile-b: #4b4a4d;
    --tile-c: #5f5048;
    --tile-d: #57595c;
  }
  * { margin: 0; padding: 0; box-sizing: border-box; }
  html, body { width: 1200px; height: 833px; overflow: hidden; background: #1a1a1c; }
  .splash { position: relative; width: 1200px; height: 833px; overflow: hidden; }
  .people-grid {
    position: absolute; inset: 0;
    display: grid;
    grid-template-columns: 301px 301px 302px 296px;
    grid-template-rows: 283px 301px 249px;
  }
  .portrait { width: 100%; height: 100%; }
  .portrait.tone-a { background: radial-gradient(circle at 50% 40%, var(--tile-a), #3a3330 75%); }
  .portrait.tone-b { background: radial-gradient(circle at 50% 40%, var(--tile-b), #2d2d30 75%); }
  .portrait.tone-c { background: radial-gradient(circle at 50% 40%, var(--tile-c), #332c29 75%); }
  .portrait.tone-d { background: radial-gradient(circle at 50% 40%, var(--tile-d), #303236 75%); }
  .veil { position: absolute; inset: 0; background: var(--veil); }
  .brand-dot {
    position: absolute; left: 566px; top: 192px;
    width: 68px; height: 68px; border-radius: 50%;
    background: var(--accent);
  }
  .rule { position: absolute; height: 1px; background: var(--rule); }
  .rule-top { left: 341px; top: 397px; width: 529px; }
  .rule-left { left: 339px; top: 526px; width: 204px; }
  .rule-right { left: 667px; top: 526px; width: 203px; }
  .site-title {
    position: absolute; left: 0; right: 0; top: 408px;
    text-align: center;
    font-family: "Questrial", sans-serif; font-weight: 400;
    font-size: 64px; line-height: 80px; color: var(--ink);
    letter-spacing: 0.5px;
  }
  .audience-label {
    position: absolute; left: 543px; width: 124px; top: 506px;
    text-align: center;
    font-family: "Questrial", sans-serif;
    font-size: 33px; line-height: 40px; color: var(--ink);
  }
  .audience-choice {
    position: absolute; top: 611px; width: 250px; height: 84px;
    border: 1px solid var(--pill-edge); border-radius: 42px;
    background: var(--pill-fill);
    display: flex; align-items: center; justify-content: center;
    font-family: "Raleway", sans-serif; font-weight: 400;
    font-size: 25px; letter-spacing: 0.5px; color: var(--accent);
    text-decoration: none;
  }
  .choice-workers { left: 329px; }
  .choice-businesses { left: 621px; }
</style>
</head>
<body>
<main class="splash">
  <div class="people-grid">
    <div class="portrait tone-a" role="img" aria-label="Portrait photo of a smiling crowd worker"></div>
    <div class="portrait tone-b" role="img" aria-label="Portrait photo of a smiling crowd worker"></div>
    <div class="portrait tone-c" role="img" aria-label="Portrait photo of a smiling crowd worker"></div>
    <div class="portrait tone-d" role="img" aria-label="Portrait photo of a smiling crowd worker"></div>
    <div class="portrait tone-c" role="img" aria-label="Portrait photo of a smiling crowd worker"></div>
    <div class="portrait tone-a" role="img" aria-label="Portrait photo of a smiling crowd worker"></div>
    <div class="portrait tone-b" role="img" aria-label="Portrait photo of a smiling crowd worker"></div>
    <div class="portrait tone-d" role="img" aria-label="Portrait photo of a smiling crowd worker"></div>
    <div class="portrait tone-d" role="img" aria-label="Portrait photo of a smiling crowd worker"></div>
    <div class="portrait tone-b" role="img" aria-label="Portrait photo of a smiling crowd worker"></div>
    <div class="portrait tone-c" role="img" aria-label="Portrait photo of a smiling crowd worker"></div>
    <div class="portrait tone-a" role="img" aria-label="Portrait photo of a smiling crowd worker"></div>
  </div>
  <div class="veil"></div>

  <span class="brand-dot" aria-hidden="true"></span>
  <div class="rule rule-top"></div>
  <h1 class="site-title">A Hive in Motion</h1>
  <div class="rule rule-left"></div>
  <p class="audience-label">FOR</p>
  <div class="rule rule-right"></div>

  <a class="audience-choice choice-workers" href="#workers">WORKERS</a>
  <a class="audience-choice choice-businesses" href="#businesses">BUSINESSES</a>
</main>
</body>
</html>
```